Tallowreed Advisory Partners Business Card Design

We have the logo we just need someone to design a modern business card design.

Name: Desmond Munkalt
Phone: 3055550148
Mobile: 9175550193
Web:www.tallowreedadvisory.example
email: dmunkalt@tallowreedadvisory.example
Company: Tallowreed Advisory Partners
Title: CEO

Address: 718 Quillmore Ave, Miami, Florida 33190

Target Market(s)

companies over 100 employees

Industry/Entity Type

Business

```html
<!DOCTYPE html>
<html lang="en">
<head>
<meta charset="utf-8">
<title>Tallowreed Advisory Partners – Business Card</title>
<link href="https://fonts.googleapis.com/css2?family=Arimo:wght@400;700&display=swap" rel="stylesheet">
<style>
  :root {
    --backdrop: #e9eaec;
    --card: #ffffff;
    --brand-blue: #3d63b6;
    --ink: #111111;
    --body-text: #444444;
    --divider: #d6d6d6;
    --band-dark: #1b2030;
    --band-blue: #4166ba;
    --white: #ffffff;
  }
  * { box-sizing: border-box; margin: 0; padding: 0; }
  html, body { width: 1200px; height: 720px; overflow: hidden; }
  body {
    background: var(--backdrop);
    font-family: "Arimo", Arial, sans-serif;
    position: relative;
  }
  .card {
    position: absolute;
    top: 237px;
    width: 488px;
    height: 280px;
    background: var(--card);
    overflow: hidden;
  }
  .card--front { left: 80px; }
  .card--back { left: 628px; }

  /* Brand lockup */
  .brand { position: absolute; text-align: center; color: var(--ink); font-weight: 700; }
  .brand__dot { display: block; margin: 0 auto; border-radius: 50%; background: var(--brand-blue); }
  .brand__name { display: block; letter-spacing: 0.5px; line-height: 1.05; }

  .card--front .brand { left: 20px; top: 83px; width: 160px; }
  .card--front .brand__dot { width: 54px; height: 54px; margin-bottom: 10px; }
  .card--front .brand__name { font-size: 15px; }
  .card--front .brand__sub { font-size: 8px; letter-spacing: 0.6px; display: block; margin-top: 2px; }

  .divider {
    position: absolute; left: 185px; top: 60px;
    width: 1px; height: 140px; background: var(--divider);
  }

  .contact { position: absolute; left: 203px; top: 61px; color: var(--body-text); font-size: 11px; line-height: 15px; }
  .contact__name { color: var(--brand-blue); font-size: 15px; line-height: 18px; }
  .contact__title { color: var(--ink); font-size: 11px; margin-bottom: 13px; }
  .contact__company { color: var(--brand-blue); font-weight: 700; margin-bottom: 2px; }
  .contact__address { margin-bottom: 6px; }
  .contact__line { display: flex; align-items: center; gap: 6px; }
  .contact__line svg { width: 11px; height: 11px; fill: var(--brand-blue); flex: none; }

  .band {
    position: absolute; left: 0; bottom: 0; width: 100%; height: 37px;
    background: linear-gradient(90deg, var(--band-dark) 0%, #2a3556 45%, var(--band-blue) 100%);
    color: var(--white);
  }
  .band__web { position: absolute; left: 76px; top: 12px; font-size: 11px; }
  .band__brand { position: absolute; right: 28px; top: 6px; text-align: center; font-weight: 700; line-height: 1.05; }
  .band__brand span { display: block; }
  .band__brand .brand__name { font-size: 14px; letter-spacing: 0.5px; }
  .band__brand .brand__sub { font-size: 6.5px; letter-spacing: 0.5px; }

  .card--back .brand { left: 0; top: 66px; width: 100%; }
  .card--back .brand__dot { width: 80px; height: 80px; margin-bottom: 16px; }
  .card--back .brand__name { font-size: 24px; letter-spacing: 0.8px; }
  .card--back .brand__sub { font-size: 10px; letter-spacing: 0.8px; display: block; margin-top: 3px; }
  .back__web { position: absolute; left: 0; top: 207px; width: 100%; text-align: center; font-size: 11px; color: var(--body-text); }
</style>
</head>
<body>

  <section class="card card--front">
    <div class="brand">
      <span class="brand__dot"></span>
      <span class="brand__name">TALLOWREED</span>
      <span class="brand__sub">ADVISORY PARTNERS</span>
    </div>

    <div class="divider"></div>

    <div class="contact">
      <p class="contact__name">Desmond Munkalt</p>
      <p class="contact__title">CEO</p>
      <p class="contact__company">Tallowreed Advisory Partners</p>
      <p class="contact__address">718 Quillmore Ave<br>Miami, Florida 33190</p>
      <p class="contact__line">
        <svg viewBox="0 0 24 24" aria-hidden="true"><path d="M3 9c0-3 4-5 9-5s9 2 9 5v2h-5V9c-1-.6-2.5-1-4-1s-3 .4-4 1v2H3V9zm3 3h12l2 8H4l2-8zm6 2a2.5 2.5 0 100 5 2.5 2.5 0 000-5z"/></svg>
        3055550148
      </p>
      <p class="contact__line">
        <svg viewBox="0 0 24 24" aria-hidden="true"><path d="M7 1h10a2 2 0 012 2v18a2 2 0 01-2 2H7a2 2 0 01-2-2V3a2 2 0 012-2zm0 3v14h10V4H7zm5 15.5a1.2 1.2 0 100 2.4 1.2 1.2 0 000-2.4z"/></svg>
        9175550193
      </p>
      <p class="contact__line">
        <svg viewBox="0 0 24 24" aria-hidden="true"><path d="M2 5h20v14H2V5zm2 2v.5l8 5.5 8-5.5V7H4zm0 3v7h16v-7l-8 5.5L4 10z"/></svg>
        dmunkalt@tallowreedadvisory.example
      </p>
    </div>

    <div class="band">
      <span class="band__web">www.tallowreedadvisory.example</span>
      <div class="band__brand">
        <span class="brand__name">TALLOWREED</span>
        <span class="brand__sub">ADVISORY PARTNERS</span>
      </div>
    </div>
  </section>

  <section class="card card--back">
    <div class="brand">
      <span class="brand__dot"></span>
      <span class="brand__name">TALLOWREED</span>
      <span class="brand__sub">ADVISORY PARTNERS</span>
    </div>
    <p class="back__web">www.tallowreedadvisory.example</p>
  </section>

</body>
</html>
```